Business Card Design Project

I require a business card for a new coaching business based in Melbourne with global clients. Both companies and individuals will retain our coaching services.

Target Market(s)

Both small business and large corporate in western speaking countries. Individuals requiring support and direction on issues such as fears, phobias, career, relationships, confidence, self esteem etc.

Industry/Entity Type

Business

Font styles to use
Sans Serif

Colors

Designer to choose colors to be used in the design.

Requirements
Must have
• White background to enhance the colours in the logo. Logo on the left.
Should not have
• The black and white version of the logo. Keep the colours.

```html
<!DOCTYPE html>
<html lang="en">
<head>
<meta charset="utf-8">
<title>Clear Path Coaching – Business Card</title>
<link rel="stylesheet" href="https://fonts.googleapis.com/css2?family=Courier+Prime:wght@400;700&display=swap">
<style>
  :root {
    --paper: #ffffff;
    --ink: #111111;
    --ink-soft: #2a2a2a;
    --logo-ink: #444444;
    --logo-dot: #e9229b;
    --card-edge: #555555;
  }
  * { box-sizing: border-box; margin: 0; padding: 0; }
  html, body {
    width: 1200px;
    height: 900px;
    overflow: hidden;
    background: var(--paper);
  }
  body {
    position: relative;
    font-family: "Courier Prime", "Courier New", monospace;
    color: var(--ink);
  }
  .side-label {
    position: absolute;
    top: 148px;
    width: 564px;
    text-align: center;
    font-size: 70px;
    font-weight: 400;
    letter-spacing: 5px;
    line-height: 1;
  }
  .side-label--front { left: 22px; top: 152px; }
  .side-label--back { left: 585px; top: 148px; }

  .card {
    position: absolute;
    top: 271px;
    width: 565px;
    height: 339px;
    border: 1px solid var(--card-edge);
    background: var(--paper);
  }
  .card--front { left: 22px; }
  .card--back { left: 613px; }

  .brand {
    position: absolute;
    left: 10px;
    top: 10px;
    display: flex;
    align-items: center;
    gap: 10px;
  }
  .brand__dot {
    width: 62px;
    height: 62px;
    border-radius: 50%;
    background: var(--logo-dot);
  }
  .brand__name {
    font-size: 19px;
    font-weight: 700;
    line-height: 20px;
    color: var(--logo-ink);
    text-transform: uppercase;
  }

  .person {
    position: absolute;
    left: 93px;
    top: 120px;
    font-size: 22px;
    line-height: 34px;
    letter-spacing: -1px;
    color: var(--ink-soft);
  }

  .contact {
    position: absolute;
    left: 10px;
    bottom: 6px;
    font-size: 18px;
    line-height: 22px;
    letter-spacing: 0.6px;
  }

  .motto {
    position: absolute;
    left: 0;
    right: 0;
    top: 120px;
    text-align: center;
    font-size: 20.5px;
    line-height: 47px;
    letter-spacing: 1.2px;
  }
</style>
</head>
<body>
  <div class="side-label side-label--front">FRONT</div>
  <div class="side-label side-label--back">BACK</div>

  <section class="card card--front">
    <div class="brand">
      <span class="brand__dot"></span>
      <span class="brand__name">Clear Path<br>Coaching</span>
    </div>

    <div class="person">
      <p class="person__name">Marla Quinlan-Hayes</p>
      <p class="person__role">Performance Consultant and Coach</p>
    </div>

    <div class="contact">
      <p>Phone: +61 (0) 400 555 019</p>
      <p>Email: marlaq456@example.com</p>
      <p>ABN: 12345678901</p>
    </div>
  </section>

  <section class="card card--back">
    <div class="motto">
      <p>The mind is more powerful than the body.</p>
      <p>Give yourself permission to shine</p>
    </div>
  </section>
</body>
</html>
```